Harrowgate Distillery Bottle Label Design

We need a label design for a product called "Cedar Lorne Straight Bourbon Whiskey". The bottle has two embossments on the side and an image printed on the back that will show through when looking from the front (shown in the attached image). It's made of 30% rye and 70% corn; images of the ingredients can be incorporated into the label design. We are a distillery that produces whiskey and bourbon from local farmers around the area. We focus on the quality of the ingredients and using the recipes passed down from generation to generation. We like a straight forward design using two colors maximum. The background will be brown once filled with the bourbon, so it must contrast against it (i.e. white and other lighter colors). The Harrowgate Distillery logo must be present on the bottle front, as well as 750 ml, 84 PROOF, 42% ALC/VOL.

Target Market(s)

Craft whiskey consumers.

Industry/Entity Type

Product

Colors
fee18a
fbe7d2
fff3d1
fefcee
fefdec
fdf9cf

Requirements
Must have
• 750 ml, 84 PROOF, 42% ALC/VOL. Aged for 3 years.The Harrowgate Distillery logo must be present on the bottle. Only two colors on label.
Nice to have
• Story of how we are a micro distillery making hand crafted whiskey.
Should not have
• False or misleading print.

```html
<!DOCTYPE html>
<html lang="en">
<head>
<meta charset="utf-8">
<title>Cedar Lorne Straight Bourbon Whiskey – Label</title>
<link rel="stylesheet" href="https://fonts.googleapis.com/css2?family=Cormorant+Garamond:wght@500;600&family=Montserrat:wght@700&display=swap">
<style>
  :root {
    --backdrop: #b8652a;
    --label-paper: #ffffff;
    --label-ink: #1f1f1f;
    --band-dark: #3b3b3b;
    --band-line: #4a4a4a;
    --accent-gold: #e6d94a;
    --text-light: #f4f4f4;
  }
  * { margin: 0; padding: 0; box-sizing: border-box; }
  html, body {
    width: 1200px;
    height: 1000px;
    overflow: hidden;
    background: var(--backdrop);
  }
  .canvas {
    width: 1200px;
    height: 1000px;
    display: flex;
    align-items: center;
    justify-content: center;
  }
  .label {
    width: 680px;
    height: 700px;
    background: var(--label-paper);
    display: flex;
    flex-direction: column;
    box-shadow: 0 6px 24px rgba(0,0,0,0.18);
  }
  .label-top {
    height: 410px;
    flex-shrink: 0;
    display: flex;
    flex-direction: column;
    align-items: center;
    padding-top: 28px;
  }
  .brand-mark {
    flex-shrink: 0;
    width: 72px;
    height: 72px;
    border-radius: 50%;
    background: var(--label-ink);
  }
  .brand-name {
    margin-top: 18px;
    font-family: "Montserrat", sans-serif;
    font-weight: 700;
    color: var(--label-ink);
    text-align: center;
    line-height: 1;
  }
  .brand-name .brand-primary {
    display: block;
    font-size: 38px;
    letter-spacing: -0.5px;
  }
  .brand-name .brand-secondary {
    display: block;
    margin-top: 8px;
    font-size: 15px;
    letter-spacing: 5px;
  }
  .title-block {
    margin-top: 22px;
    width: 100%;
    display: flex;
    flex-direction: column;
    align-items: center;
  }
  .title-rule {
    display: block;
    flex-shrink: 0;
    width: 560px;
    height: 16px;
  }
  .product-name {
    font-family: "Cormorant Garamond", serif;
    font-weight: 500;
    font-size: 84px;
    letter-spacing: 1px;
    white-space: nowrap;
    text-align: center;
    color: var(--label-ink);
    line-height: 1;
    margin: 14px 0 10px;
  }
  .label-band {
    flex: 1;
    background: var(--band-dark);
    border-top: 4px solid var(--band-line);
    display: flex;
    flex-direction: column;
    align-items: center;
    padding-top: 24px;
    color: var(--text-light);
  }
  .product-type {
    font-family: "Cormorant Garamond", serif;
    font-weight: 500;
    font-size: 42px;
    line-height: 1.1;
    text-align: center;
  }
  .age-statement {
    margin-top: 18px;
    font-family: "Cormorant Garamond", serif;
    font-weight: 500;
    color: var(--accent-gold);
    font-size: 36px;
    display: flex;
    align-items: baseline;
    gap: 10px;
  }
  .age-statement .age-number {
    font-size: 96px;
    line-height: 0.8;
  }
  .bottle-facts {
    margin-top: 22px;
    font-family: "Cormorant Garamond", serif;
    font-weight: 600;
    font-size: 17px;
    letter-spacing: 0.5px;
  }
</style>
</head>
<body>
  <main class="canvas">
    <section class="label">
      <div class="label-top">
        <span class="brand-mark" aria-hidden="true"></span>
        <p class="brand-name">
          <span class="brand-primary">Harrowgate</span>
          <span class="brand-secondary">DISTILLERY</span>
        </p>
        <div class="title-block">
          <svg class="title-rule" viewBox="0 0 560 16" aria-hidden="true">
            <line x1="0" y1="8" x2="560" y2="8" stroke="#1f1f1f" stroke-width="1.5"/>
            <rect x="274" y="2" width="12" height="12" transform="rotate(45 280 8)" fill="#1f1f1f"/>
          </svg>
          <h1 class="product-name">CEDAR LORNE</h1>
          <svg class="title-rule" viewBox="0 0 560 16" aria-hidden="true">
            <line x1="0" y1="8" x2="560" y2="8" stroke="#1f1f1f" stroke-width="1.5"/>
            <rect x="274" y="2" width="12" height="12" transform="rotate(45 280 8)" fill="#1f1f1f"/>
          </svg>
        </div>
      </div>
      <div class="label-band">
        <p class="product-type">Straight Bourbon<br>Whiskey</p>
        <p class="age-statement"><span>Aged</span><span class="age-number">3</span><span>Years</span></p>
        <p class="bottle-facts">750 ML | 84 PROOF | 42% ALC/VOL</p>
      </div>
    </section>
  </main>
</body>
</html>
```